Webdesign für regionales Bauunternehmen / KVR
Zielgruppe
Die Firma KVR, als regionales Bauunternehmen, plant und gestaltet die Lebensräume von Menschen, die sich zum Bau ihrer eigenen vier Wände entschlossen haben. Von der „grünen Wiese“ bis zum Richtfest und darüber hinaus werden die Bauherren unterstützt. Die Wünsche der Kunden reichen dabei von Barrierefreiheit, der Anwendung ökologischer und kostenbewusster Baukonzepte bis zu familienfreundlichen Lösungen im Einfamilien- oder Mehrgenerationenhausbau.
Komplettleistungen sind die Stärke des Unternehmens. Das Leistungsprofil umfasst zudem auch alle Arbeiten im Hoch- und Tiefbau, bei Trockenlegungen und bei der Sanierung von Baudenkmälern sowie Altbauten. Als mittelständischer Baubetrieb ist die Firma sowohl für Privatpersonen als auch für Gewerbetreibende und Kommunen tätig.
Aufgabenstellung
Nur die Startseite layouten
n Photoshop
siehe auch 'unsere Vorstellungen'
Slogan: Vielefalt unter einem Dach ; Kompetenz in der Region
ACHTUNG: Es gibt 2 Logos, das Hauptlogo ist das kvr.ipg ; das Hausbau-Logo muss im Verbund mit dem KVR-Logo dargestellt werden.
geeignete referenzbilder liegen nicht vor. Die Konzentration sollte auf EFH und EFM liegen. (bitte bei Auswahl der Stock-Bilder beachten)
INSTA-Logo einbinden

```html
<!DOCTYPE html>
<html lang="de">
<head>
<meta charset="utf-8">
<title>KVR Tiefbau Hochbau – Startseite</title>
<link href="https://fonts.googleapis.com/css2?family=Open+Sans:wght@300;400;600;700&display=swap" rel="stylesheet">
<style>
  :root {
    --yellow: #f5c410;
    --dark: #4a4c51;
    --text-dark: #3d3f44;
    --white: #ffffff;
    --footer-text: #4f5156;
  }
  * { margin: 0; padding: 0; box-sizing: border-box; }
  html, body { width: 1200px; height: 2175px; overflow: hidden; background: var(--white); }
  body { font-family: "Open Sans", sans-serif; color: var(--text-dark); position: relative; }
  .abs { position: absolute; }

  /* Header */
  .site-header { position: absolute; left: 0; top: 0; width: 1200px; height: 149px; }
  .brand-main { left: 55px; top: 66px; font-size: 22px; font-weight: 700; color: var(--text-dark); letter-spacing: 1px; display: flex; align-items: center; gap: 8px; }
  .brand-main .mark { width: 12px; height: 12px; background: var(--yellow); }
  .brand-main small { font-size: 11px; font-weight: 400; line-height: 1.1; letter-spacing: 0.5px; }
  .main-nav a { position: absolute; top: 74px; font-size: 13px; letter-spacing: 0.8px; color: var(--text-dark); text-decoration: none; }
  .brand-house { left: 1010px; top: 68px; font-size: 14px; font-weight: 700; color: var(--text-dark); letter-spacing: 0.6px; display: flex; align-items: center; gap: 8px; }
  .brand-house .mark { width: 12px; height: 12px; border-radius: 50%; background: var(--yellow); }

  /* Sections */
  .band { position: absolute; left: 0; width: 1200px; height: 452px; }
  .panel { position: absolute; top: 0; height: 100%; background: var(--dark); }
  .photo { position: absolute; top: 0; height: 100%; }
  .headline { position: absolute; font-weight: 300; color: var(--yellow); font-size: 39px; line-height: 41px; }
  .lead { position: absolute; font-size: 12.6px; line-height: 19.3px; letter-spacing: 0.5px; color: var(--white); }
  .btn { position: absolute; height: 37px; background: var(--yellow); color: var(--text-dark); font-weight: 700; font-size: 13.5px; letter-spacing: 0.7px; display: flex; align-items: center; justify-content: center; text-decoration: none; }

  .slider-caption { position: absolute; left: 519px; top: 21px; color: var(--white); font-size: 12.5px; letter-spacing: 0.5px; text-decoration: underline; }
  .slider-arrow { position: absolute; top: 205px; }
  .slider-dots { position: absolute; left: 773px; top: 419px; display: flex; gap: 8.5px; }
  .slider-dots span { width: 14px; height: 14px; border-radius: 50%; background: var(--white); }
  .slider-dots span.active { background: var(--yellow); }

  /* Footer */
  .footer-col { position: absolute; top: 2005px; font-size: 12.6px; line-height: 19.3px; letter-spacing: 0.6px; color: var(--footer-text); }
  .footer-col strong { font-weight: 700; }
  .partner-badge { position: absolute; background: #d9dcd6; border-radius: 3px; }
  .legal { position: absolute; top: 2150px; font-size: 11px; letter-spacing: 0.6px; color: var(--footer-text); }
  .legal a { color: var(--footer-text); }
</style>
</head>
<body>

<header class="site-header">
  <div class="abs brand-main"><span class="mark"></span>KVR <small>TIEFBAU<br>HOCHBAU</small></div>
  <nav class="main-nav">
    <a href="#" style="left:228px">Tiefbau</a>
    <a href="#" style="left:313px">Hochbau</a>
    <a href="#" style="left:406px">Referenzen</a>
    <a href="#" style="left:515px">Unternehmen</a>
    <a href="#" style="left:643px">Stellenangebote</a>
    <a href="#" style="left:785px">Grundstücke</a>
    <a href="#" style="left:904px">Kontakt</a>
  </nav>
  <div class="abs brand-house"><span class="mark"></span>KVR Hausbau GmbH</div>
</header>

<section class="band" style="top:149px">
  <div class="panel" style="left:0;width:394px"></div>
  <h1 class="headline" style="left:51px;top:54px">Unser Service<br>wird Sie<br>überzeugen.</h1>
  <p class="lead" style="left:51px;top:192px;width:310px">Seit 20 Jahren steht Veränderung im Mittelpunkt unseres Schaffens als modernes und innovatives Bauunternehmen in der Erzgebirgsregion. Ob Bauantrag, Finanzierung oder die Gestaltung der Grundrisse: Wir sind Ihr Partner und informieren Sie gern zu all Ihren Fragen.</p>
  <a class="btn" href="#" style="left:50px;top:345px;width:163px">Unternehmen</a>
  <div class="photo" role="img" aria-label="Junge Familie spielt im neuen Wohnzimmer mit ihrem Kind" style="left:394px;width:368px;background:linear-gradient(160deg,#e4e2df 0%,#cfc9c2 45%,#9aa3b0 75%,#c9c3bb 100%)"></div>
  <div class="photo" role="img" aria-label="Modernes weißes Einfamilienhaus mit gelber Fassadenfläche auf grünem Rasen" style="left:762px;width:438px;background:linear-gradient(180deg,#b7cde4 0%,#dfe6ec 40%,#e9e9e6 62%,#8fae4a 84%,#7ea03c 100%)"></div>
</section>

<section class="band" style="top:606px">
  <div class="photo" role="img" aria-label="Zwei Bauarbeiter in Warnwesten halten einen Bauplan gegen den Himmel" style="left:0;width:708px;background:linear-gradient(180deg,#aebfd6 0%,#d9d2cf 35%,#cbbdb6 65%,#c7c95a 90%,#6d6f56 100%)"></div>
  <div class="panel" style="left:708px;width:492px"></div>
  <h2 class="headline" style="left:792px;top:110px">Ob tief oder hoch –<br>mit uns können Sie<br>bauen.</h2>
  <p class="lead" style="left:792px;top:245px;width:330px">Egal, ob Hoch, Tief oder Weit - wir bauen mit Ihnen verantwortungsvoll an Ihrem Projekt.</p>
  <a class="btn" href="#" style="left:792px;top:301px;width:111px">Tiefbau</a>
  <a class="btn" href="#" style="left:918px;top:301px;width:111px">Hochbau</a>
</section>

<section class="band" style="top:1062px">
  <div class="panel" style="left:0;width:492px"></div>
  <h2 class="headline" style="left:112px;top:114px">Unsere<br>Referenzen</h2>
  <p class="lead" style="left:112px;top:200px;width:300px">Eine Auswahl unserer bereits realisierten Bauprojekte. In unseren Referenzen finden Sie vom Einfamilienhaus oder Mehrfamilenhäuser alles.</p>
  <a class="btn" href="#" style="left:112px;top:290px;width:130px">Referenzen</a>
  <div class="photo" role="img" aria-label="Weißes Einfamilienhaus mit dunklem Satteldach, Garage und gepflasterter Einfahrt" style="left:492px;width:708px;background:linear-gradient(180deg,#a9c7e3 0%,#d6e2ec 30%,#e6e6e2 55%,#6f9b3c 78%,#cfcbc4 100%)">
    <a class="slider-caption" href="#">EFH / MFH - Kompakt und familienfreundlich</a>
    <svg class="slider-arrow" style="left:12px" width="28" height="44" viewBox="0 0 28 44"><polyline points="22,4 6,22 22,40" fill="none" stroke="var(--yellow)" stroke-width="5"/></svg>
    <svg class="slider-arrow" style="left:667px" width="28" height="44" viewBox="0 0 28 44"><polyline points="6,4 22,22 6,40" fill="none" stroke="var(--yellow)" stroke-width="5"/></svg>
    <div class="slider-dots" style="left:281px"><span class="active"></span><span></span><span></span><span></span><span></span><span></span><span></span></div>
  </div>
</section>

<section class="band" style="top:1519px">
  <div class="photo" role="img" aria-label="Kleines blaues Holzhaus mit weißem Dach neben einer jungen Pflanze in Erde" style="left:0;width:708px;background:linear-gradient(160deg,#9cc45a 0%,#7fb04a 40%,#3f82c4 60%,#5a4130 85%,#3b2b20 100%)"></div>
  <div class="panel" style="left:708px;width:492px"></div>
  <h2 class="headline" style="left:792px;top:109px">Wir kaufen Ihr<br>Grundstück.</h2>
  <p class="lead" style="left:792px;top:202px;width:280px">Wir kaufen bebaute und unbebaute Grundstücke. Dabei stehen wir seit über 20 Jahren für eine sichere und diskrete Abwicklung.</p>
  <a class="btn" href="#" style="left:792px;top:301px;width:146px">Grundstücke</a>
</section>

<footer>
  <div class="footer-col" style="left:25px"><strong>KVR Tannenbach</strong><br>Lindenweg 12<br>09210 Tannenbach</div>
  <div class="footer-col" style="left:216px">Tel. 030100 - 555 25<br>Fax 030100 - 555 21<br>info(at)kvr-tannenbach(dot)de</div>
  <div class="partner-badge" style="left:739px;top:2005px;width:100px;height:50px"></div>
  <div class="partner-badge" style="left:868px;top:2009px;width:44px;height:44px"></div>
  <div class="partner-badge" style="left:949px;top:2008px;width:200px;height:46px"></div>
  <div class="legal" style="left:318px">© 2022 KVR Tannenbach</div>
  <div class="legal" style="left:518px"><a href="#">Impressum</a></div>
  <div class="legal" style="left:654px"><a href="#">Datenschutz</a></div>
  <div class="legal" style="left:817px"><a href="#">Kontakt</a></div>
</footer>

</body>
</html>
```